We operate a niche online Job Board in Australia. The website is called 'Harvest Roles Australia' and is used by Christian Employers to advertise their job vacancies.
I would like a business card that identifies with our website (www.harvestroles-example.com.au). We would like the same colors and fonts used on our business card from our website. When people look at our business card we want them to be able to recognise it from the website.
We want the web address to be dominant.
Updates
We are liking those that use white space as well as the blue and orange and those that highlight the url.
We now have 60 designs and therefore will not wait for the Sunday deadline to make a decision. We have a few we like.
The ones we like are:
- bold
- creative
- colorful (blue orange and white)
- some white space
- no boxes or borders
- font the same as our website
- reflects the look of our website
We will make a final decision in the next 6 hours so please if you think you have something to offer then get it in within the next 6 hours. If you think you will leave it till later you will miss out. Thanks to all those who have responded with some great designs, sorry we can't reward all of you!
Industry/Entity Type
Business
Contact Information for Business Card
Harvest Roles Australia
www.harvestroles-example.com.au
Peter Galvridge
CEO
Phone: 1300 512 874
Mobile: 0412 735019
Fax: (03) 9157 2360
email: peter@harvestroles-example.com.au
Requirements
Should not have
- We do not want a cross or any cliche christian images.

```html
<!DOCTYPE html>
<html lang="en">
<head>
<meta charset="utf-8">
<title>Harvest Roles Australia – Business Card</title>
<link rel="stylesheet" href="https://fonts.googleapis.com/css2?family=Cormorant+Garamond:ital,wght@1,500;1,700&family=Libre+Baskerville&family=Pinyon+Script&display=swap">
<style>
  :root {
    --card-white: #ffffff;
    --card-peach: #fddcb8;
    --card-apricot: #f9b56a;
    --card-orange: #f5921e;
    --ink: #111111;
    --rule-red: #e8252a;
    --url-blue: #1a5aa6;
    --quote-grey: #4f433b;
  }
  html, body {
    margin: 0;
    padding: 0;
    width: 1200px;
    height: 693px;
    overflow: hidden;
    background: var(--card-white);
  }
  .card {
    position: relative;
    width: 1200px;
    height: 693px;
    overflow: hidden;
    background: linear-gradient(100deg, var(--card-white) 0%, var(--card-peach) 32%, var(--card-apricot) 72%, var(--card-orange) 100%);
    color: var(--ink);
  }
  .brand-name {
    position: absolute;
    left: 0;
    width: 1200px;
    top: 168px;
    margin: 0;
    text-align: center;
    font-family: "Cormorant Garamond", "Times New Roman", serif;
    font-style: italic;
    font-weight: 500;
    font-size: 112px;
    line-height: 1;
    letter-spacing: 1px;
    color: var(--ink);
  }
  .brand-rule {
    position: absolute;
    left: 118px;
    top: 300px;
    width: 974px;
    height: 8px;
  }
  .brand-url {
    position: absolute;
    left: 0;
    width: 1200px;
    top: 318px;
    margin: 0;
    text-align: center;
    font-family: "Cormorant Garamond", "Times New Roman", serif;
    font-style: italic;
    font-weight: 700;
    font-size: 50px;
    line-height: 1.2;
    color: var(--url-blue);
  }
  .contact {
    position: absolute;
    left: 65px;
    top: 502px;
    font-family: "Libre Baskerville", "Times New Roman", serif;
  }
  .contact-name {
    margin: 0 0 4px;
    font-size: 26px;
    font-weight: 400;
    line-height: 1.2;
  }
  .contact-list {
    margin: 0;
    padding: 0;
    list-style: none;
    font-size: 18px;
    line-height: 28px;
  }
  .scripture {
    position: absolute;
    left: 618px;
    top: 452px;
    margin: 0;
    width: 520px;
    font-family: "Pinyon Script", cursive;
    font-size: 29px;
    line-height: 39px;
    color: var(--quote-grey);
  }
  .scripture p { margin: 0; }
  .scripture .indent { padding-left: 8px; }
  .scripture cite {
    display: block;
    text-align: right;
    font-style: normal;
    padding-right: 30px;
    margin-top: 0;
  }
</style>
</head>
<body>
  <main class="card">
    <h1 class="brand-name">Harvest Roles Australia</h1>
    <svg class="brand-rule" viewBox="0 0 974 8" aria-hidden="true">
      <path d="M0 4 Q487 -1 974 4 Q487 9 0 4 Z" fill="var(--rule-red)"/>
    </svg>
    <p class="brand-url">www.harvestroles-example.com.au</p>

    <section class="contact">
      <h2 class="contact-name">Peter Galvridge CEO</h2>
      <ul class="contact-list">
        <li>Phone: 1300 512 874</li>
        <li>Mobile: 0412 735019</li>
        <li>Fax: (03) 9157 2360</li>
        <li>E-mail: peter@harvestroles-example.com.au</li>
      </ul>
    </section>

    <blockquote class="scripture">
      <p>`...it is a good thing to receive wealth from</p>
      <p>God and the good health to enjoy it.</p>
      <p>To enjoy your work and accept your lot in life</p>
      <p class="indent">-- that is indeed a gift from God...’</p>
      <cite>Ecclesiastes 5:19</cite>
    </blockquote>
  </main>
</body>
</html>
```